real estate business card
DR Horvath Company, Inc
Professional
Daniel Horvath
President
318 Birchwood St. #2207
Harbor Point, Ma 02196
Dan@drhorvathcompany.com
drhorvathcompany.com

```html
<!DOCTYPE html>
<html lang="en">
<head>
<meta charset="utf-8">
<title>DR Horvath Company, Inc — Business Card</title>
<link href="https://fonts.googleapis.com/css2?family=Cormorant+SC:wght@500;600&display=swap" rel="stylesheet">
<style>
  :root {
    --stage: #d9dadc;
    --card: #ffffff;
    --brand-blue: #1a73c4;
    --brand-blue-deep: #0b4f9a;
    --brand-blue-light: #4fb0ee;
    --ink: #5d6066;
    --ink-soft: #8a8d93;
    --rule: #b9bcc1;
  }
  * { margin: 0; padding: 0; box-sizing: border-box; }
  html, body {
    width: 1200px; height: 984px; overflow: hidden;
    background: var(--stage);
  }
  .sheet { position: relative; width: 1200px; height: 984px; }
  .card {
    position: absolute; left: 220px;
    width: 760px; height: 434px;
    background: var(--card);
    border-radius: 26px;
    overflow: hidden;
    box-shadow: 0 10px 28px rgba(0,0,0,0.18);
  }
  .card--back { top: 40px; }
  .card--front { top: 510px; }

  /* company name */
  .brand { display: flex; align-items: center; gap: 16px; }
  .brand__dot {
    flex: none; border-radius: 50%;
    background: var(--brand-blue);
  }
  .brand__name {
    font-family: "Cormorant SC", serif; font-weight: 600;
    color: var(--brand-blue); line-height: 1.1; white-space: nowrap;
  }

  /* back face */
  .card--back .brand {
    position: absolute; left: 0; right: 0; top: 196px; justify-content: center;
  }
  .card--back .brand__dot { width: 22px; height: 22px; }
  .card--back .brand__name { font-size: 36px; letter-spacing: 1px; }
  .back__web {
    position: absolute; left: 70px; bottom: 52px;
    font-family: "Cormorant SC", serif; font-weight: 600;
    font-size: 16px; letter-spacing: 5px; color: var(--ink);
  }

  /* front face */
  .card--front .brand {
    position: absolute; left: 0; right: 0; top: 50px; justify-content: center;
  }
  .card--front .brand__dot { width: 18px; height: 18px; }
  .card--front .brand__name { font-size: 34px; letter-spacing: 1px; }

  .person {
    position: absolute; left: 70px; top: 150px; width: 250px;
    text-align: right;
    font-family: "Cormorant SC", serif; font-weight: 600; color: var(--ink);
  }
  .person__name { font-size: 19px; letter-spacing: 1.5px; color: var(--brand-blue-deep); }
  .person__title { font-size: 15px; letter-spacing: 1.5px; color: var(--ink-soft); margin-bottom: 14px; }
  .person__address { font-size: 15px; letter-spacing: 1px; line-height: 1.35; }

  .divider {
    position: absolute; left: 338px; top: 146px; width: 1px; height: 116px;
    background: var(--rule);
  }
  .contacts {
    position: absolute; left: 356px; top: 146px; list-style: none;
    font-family: "Cormorant SC", serif; font-weight: 600;
    font-size: 15px; letter-spacing: 1px; color: var(--ink);
  }
  .contacts li { display: flex; align-items: center; gap: 10px; height: 29px; }
  .contacts svg { width: 16px; height: 16px; flex: none; }

  .band {
    position: absolute; left: 0; bottom: 0; width: 760px; height: 120px;
    background: linear-gradient(90deg, var(--brand-blue-deep), var(--brand-blue) 55%, var(--brand-blue-light));
  }
</style>
</head>
<body>
<main class="sheet">

  <section class="card card--back" aria-label="Card back">
    <div class="brand">
      <span class="brand__dot"></span>
      <span class="brand__name">DR Horvath Company, Inc</span>
    </div>
    <p class="back__web">www.drhorvathcompany.com</p>
  </section>

  <section class="card card--front" aria-label="Card front">
    <div class="brand">
      <span class="brand__dot"></span>
      <span class="brand__name">DR Horvath Company, Inc</span>
    </div>

    <div class="person">
      <p class="person__name">Daniel Horvath</p>
      <p class="person__title">President</p>
      <p class="person__address">318 Birchwood St. #2207<br>Harbor Point, MA 02196</p>
    </div>

    <span class="divider"></span>

    <ul class="contacts">
      <li>
        <svg viewBox="0 0 16 16"><circle cx="8" cy="8" r="8" fill="#5d6066"/><path d="M5.2 4.2l1.4-.3.8 2-1 .8a5 5 0 0 0 2.4 2.4l.8-1 2 .8-.3 1.4c-3.4.4-6.5-2.7-6.1-6.1z" fill="#fff"/></svg>
        1-877-204-5518
      </li>
      <li>
        <svg viewBox="0 0 16 16"><circle cx="8" cy="8" r="8" fill="#5d6066"/><path d="M5.2 4.2l1.4-.3.8 2-1 .8a5 5 0 0 0 2.4 2.4l.8-1 2 .8-.3 1.4c-3.4.4-6.5-2.7-6.1-6.1z" fill="#fff"/></svg>
        508-362-9041
      </li>
      <li>
        <svg viewBox="0 0 16 16"><circle cx="8" cy="8" r="8" fill="#5d6066"/><rect x="4" y="5" width="8" height="6" fill="none" stroke="#fff" stroke-width="1.2"/><path d="M4 5l4 3.4L12 5" fill="none" stroke="#fff" stroke-width="1.2"/></svg>
        Dan@drhorvathcompany.com
      </li>
      <li>
        <svg viewBox="0 0 16 16"><circle cx="8" cy="8" r="8" fill="#5d6066"/><circle cx="8" cy="8" r="4" fill="none" stroke="#fff" stroke-width="1.1"/><path d="M4 8h8M8 4c-2 2.4-2 5.6 0 8M8 4c2 2.4 2 5.6 0 8" fill="none" stroke="#fff" stroke-width="1"/></svg>
        www.drhorvathcompany.com
      </li>
    </ul>

    <div class="band" role="img" aria-label="Blue decorative band along the card's lower edge"></div>
  </section>

</main>
</body>
</html>
```